Admin Backend Redesign

We need a redesign for our backend which supoosed to make the backoffice look more modern!

I will add screenshots of the backoffice so you know what data will be shown in the Admin.

Have in mind that the users of this backend are Doctors. We need a clinical look, modern and sharp. The backoffice is responsive, have that in mind. We need the backoffice to look as professional as possible.

The theme used for the website is: http://velmora.quillstack-sample.com/

ON the main page of the backoffice, under every widget i need some space to write an explanation what the widget is about.

The color code used in our logo and website is #57aad4 combined with white.

We are open for ideas!
Updates

Project Deadline Extended
Reason: Designs are ok, but nothing innovative. Please use more modern designs!

Project Deadline Extended
Reason: Havent recieved a perfect design yet. Please read instructions carefully! Thank you

Project Deadline Extended
Reason: Hey everybody, sorry for the delay. We will decide in 3 days. If anyone wants to add a Design, that would be great.

Target Market(s)

Doctors, therapists

Industry/Entity Type

It Professional

Font styles to use
Sans Serif

Requirements
Must have
• Must look uptodate, modern, like new back offices look nowadays

```html
<!DOCTYPE html>
<html lang="de">
<head>
<meta charset="utf-8">
<title>Medivio Backoffice</title>
<link href="https://fonts.googleapis.com/css2?family=Roboto:wght@400;500;700&display=swap" rel="stylesheet">
<style>
:root{
  --page:#2b2d36;
  --sidebar:#2b2d36;
  --main:#eceef0;
  --panel-head:#2f323b;
  --teal:#41c3b0;
  --teal-soft:#72d1bd;
  --blue:#57aad4;
  --text:#333;
  --muted:#666;
  --line:#e4e4e4;
  --white:#fff;
}
*{box-sizing:border-box;margin:0;padding:0}
html,body{width:880px;height:1200px;overflow:hidden}
body{background:var(--page);font-family:"Roboto",Arial,sans-serif;color:var(--text);position:relative}
.header{position:absolute;left:40px;top:0;width:800px;height:48px;background:linear-gradient(90deg,#45b5a6 0%,#4aaebd 50%,#5aa9cf 100%);color:#fff}
.brand{position:absolute;left:24px;top:15px;font-size:15px}
.user{position:absolute;right:18px;top:16px;display:flex;align-items:center;gap:8px;font-size:12px}
.avatar{width:20px;height:20px;background:#e8e8e8;border:1px solid #fff}
.sidebar{position:absolute;left:40px;top:48px;width:146px;height:1130px;background:var(--sidebar)}
.menu-toggle{position:absolute;left:109px;top:13px;width:22px;height:20px;border:1px solid #555;background:#22252c;border-radius:2px}
.menu-toggle i{position:absolute;left:5px;width:10px;height:2px;background:var(--teal)}
.nav{position:absolute;top:48px;left:0;width:146px;list-style:none}
.nav li{height:37px;display:flex;align-items:center;gap:6px;padding-left:7px;color:#fff;font-size:11px;border-bottom:1px solid #1f2127}
.nav li.active{background:linear-gradient(90deg,#40c2ae,#4caed0)}
.main{position:absolute;left:186px;top:48px;width:654px;height:1130px;background:var(--main)}
.crumb{height:30px;background:#f2f3f4;border-bottom:1px solid #ddd;display:flex;align-items:center;gap:5px;padding-left:19px;font-size:10px}
.hero{position:absolute;top:49px;width:298px;height:91px;border-radius:8px;overflow:hidden;color:#fff}
.hero .photo{position:absolute;inset:0}
.hero h2{position:absolute;left:23px;top:16px;font-size:25px;font-weight:400}
.hero p{position:absolute;left:23px;top:42px;font-size:12px}
.hero .bar{position:absolute;left:0;bottom:0;width:100%;height:27px;background:rgba(40,42,50,.8);display:flex;align-items:center;gap:5px;padding-left:24px;font-size:10px;font-weight:700}
.panel{position:absolute;width:298px;background:#fff;border:1px solid #d8d8d8}
.panel-head{height:34px;background:var(--panel-head);color:#fff;font-size:12px;padding:12px 0 0 16px;margin:1px}
.search{height:32px;background:var(--teal-soft);margin:0 1px;display:flex;align-items:center;padding-left:16px;gap:9px;color:#fff;font-size:10px;font-weight:700}
.search span{width:146px;height:21px;background:#fff;border:1px solid #bbb}
table{width:100%;border-collapse:collapse;font-size:8px;color:var(--muted)}
th{font-weight:400;color:var(--text);font-size:9.5px;text-align:left;height:30px;padding-left:16px;border-bottom:1px solid var(--line);vertical-align:bottom;padding-bottom:5px}
td{height:16px;padding-left:16px;border-bottom:1px solid #eee}
.sort{color:#bbb;font-size:7px;float:right;margin-right:6px}
.sort.on{color:var(--teal)}
.foot{position:absolute;left:16px;bottom:12px;font-size:8px}
.pager{position:absolute;right:10px;bottom:10px;display:flex;border:1px solid #ccc;font-size:7px;height:18px}
.pager span{padding:0 6px;display:flex;align-items:center;color:#666;border-right:1px solid #ddd}
.pager .cur{background:var(--teal);color:#fff}
.meter{display:inline-block;width:42px;height:5px;background:#e3e3e3;vertical-align:middle}
.meter b{display:block;height:5px;background:var(--teal)}
.legend{position:absolute;font-size:7px;color:#666;line-height:14.5px;background:#f7f7f7;padding:2px 6px}
.legend i{display:inline-block;width:9px;height:7px;margin-right:3px;vertical-align:middle}
.copy{position:absolute;left:67px;top:1183px;font-size:8px;color:#888}
</style>
</head>
<body>
<header class="header">
  <div class="brand">Header Name (logo)</div>
  <div class="user"><span class="avatar"></span>Dr.<span style="margin-left:10px">▾</span></div>
</header>

<aside class="sidebar">
  <div class="menu-toggle"><i style="top:5px"></i><i style="top:9px"></i><i style="top:13px"></i></div>
  <ul class="nav">
    <li class="active"><svg width="20" height="14" viewBox="0 0 20 14"><path d="M2 12a8 8 0 0 1 16 0" fill="none" stroke="#fff" stroke-width="2"/><path d="M10 12l4-5" stroke="#fff" stroke-width="2"/></svg>Dashboard</li>
    <li><svg width="18" height="16" viewBox="0 0 18 16"><circle cx="7" cy="4" r="3" fill="#fff"/><path d="M1 15c0-5 3-7 6-7s6 2 6 7z" fill="#fff"/></svg>Main Konto</li>
    <li><svg width="20" height="18" viewBox="0 0 20 18"><ellipse cx="10" cy="8" rx="8.5" ry="6.5" fill="none" stroke="#fff" stroke-width="1.8"/><path d="M4 13l-2 4 5-2" fill="#fff"/></svg>Patientenbewertungen</li>
  </ul>
</aside>

<main class="main">
  <div class="crumb"><svg width="12" height="11" viewBox="0 0 12 11"><path d="M6 0L0 5.5h1.8V11h3V7.5h2.4V11h3V5.5H12z" fill="#333"/></svg>Start ›</div>

  <section class="hero" style="left:20px">
    <div class="photo" role="img" aria-label="Foto: Arzt mit Stethoskop" style="background:linear-gradient(90deg,#34b9a4 0%,#44bdae 45%,#cfe6e3 75%,#9dd3cc 100%)"></div>
    <h2>Profil</h2><p>Profil bearbeiten</p>
    <div class="bar"><svg width="14" height="14" viewBox="0 0 14 14"><circle cx="7" cy="7" r="6" fill="none" stroke="#fff" stroke-width="1.5"/><path d="M6 4l3 3-3 3" fill="none" stroke="#fff" stroke-width="1.5"/></svg>WEITER</div>
  </section>
  <section class="hero" style="left:336px">
    <div class="photo" role="img" aria-label="Foto: Blutdruckmessgerät am Handgelenk" style="background:linear-gradient(90deg,#1ba79a 0%,#2aa6b2 50%,#4e5d6a 75%,#c8a795 100%)"></div>
    <h2>Patienten</h2><p>Patienten verwalten</p>
    <div class="bar"><svg width="14" height="14" viewBox="0 0 14 14"><circle cx="7" cy="7" r="6" fill="none" stroke="#fff" stroke-width="1.5"/><path d="M6 4l3 3-3 3" fill="none" stroke="#fff" stroke-width="1.5"/></svg>ALLE ANSEHEN</div>
  </section>

  <section class="panel" style="left:20px;top:162px;height:216px">
    <div class="panel-head">Wilkommen: Dr. Mustermann</div>
    <p style="font-size:9px;margin:20px 0 0 17px">Der Status Ihres offentlichen Profits ist derzeit: <span style="background:var(--teal);color:#fff;font-weight:700;font-size:8px;padding:3px 6px;border-radius:2px">Alles OK</span></p>
    <p style="font-size:7.8px;color:var(--muted);line-height:12.8px;margin:18px 20px 0 21px">Lorem ipsum dolor sit amet, consectetur adipiscing elit. Duis convallis turpis ac elementum consectetur. Cras egestas non lacus eget vestibulum. Vestibulum sodales nunc eget sem consectetur, eu tempor est gravida. Sed ut ante eget augue vulputate.</p>
  </section>

  <section class="panel" style="left:336px;top:162px;height:216px">
    <div class="panel-head">Rankora Trend fur</div>
    <svg width="276" height="164" viewBox="0 0 276 164" style="margin:10px 0 0 10px;font-size:6px" fill="#666">
      <rect x="0" y="0" width="276" height="164" fill="#f8f8f8"/>
      <rect x="16" y="4" width="252" height="134" fill="#fff" stroke="#6dd0c1" stroke-width=".8"/>
      <g stroke="#e6e6e6" stroke-width=".6">
        <line x1="16" y1="49" x2="268" y2="49"/><line x1="16" y1="93" x2="268" y2="93"/>
        <line x1="48" y1="4" x2="48" y2="138"/><line x1="82" y1="4" x2="82" y2="138"/><line x1="115" y1="4" x2="115" y2="138"/><line x1="149" y1="4" x2="149" y2="138"/><line x1="183" y1="4" x2="183" y2="138"/><line x1="216" y1="4" x2="216" y2="138"/><line x1="248" y1="4" x2="248" y2="138"/>
      </g>
      <text x="4" y="7">15</text><text x="4" y="52">10</text><text x="7" y="96">5</text><text x="7" y="140">0</text>
      <text x="35" y="151">Oct 2012</text><text x="69" y="151">Jan 2013</text><text x="102" y="151">Apr 2013</text><text x="136" y="151">Jul 2013</text><text x="169" y="151">Oct 2013</text><text x="203" y="151">Jan 2014</text><text x="236" y="151">Apr 2014</text>
      <path d="M147 138L150 60L152 55L155 58L158 56L160 14L163 20L166 45L169 60L172 70L175 66L178 75L181 72L184 70L187 75L190 62L193 70L196 66L199 71L202 64L205 70L208 66L211 70L214 67L217 72L220 70L224 70L228 68L232 69L236 66L240 68L244 63L248 65L251 61L253 64" fill="none" stroke="#e3b448" stroke-width="1.2"/>
    </svg>
  </section>

  <section class="panel" style="left:20px;top:395px;height:216px">
    <div class="panel-head">Pie 1</div>
    <div style="position:absolute;left:69px;top:52px;width:158px;height:138px;background:#f7f7f7"></div>
    <svg width="136" height="136" viewBox="0 0 42 42" style="position:absolute;left:74px;top:53px">
      <g transform="rotate(-90 21 21)" fill="none" stroke-width="20">
        <circle cx="21" cy="21" r="10" pathLength="100" stroke="#4168e8" stroke-dasharray="47.5 52.5"/>
        <circle cx="21" cy="21" r="10" pathLength="100" stroke="#f7cfac" stroke-dasharray="15 85" stroke-dashoffset="-47.5"/>
        <circle cx="21" cy="21" r="10" pathLength="100" stroke="#48cacb" stroke-dasharray="37.5 62.5" stroke-dashoffset="-62.5"/>
      </g>
    </svg>
    <div class="legend" style="left:232px;top:51px"><i style="background:#4168e8"></i>Series1<br><i style="background:#f7cfac"></i>Series2<br><i style="background:#48cacb"></i>Series3</div>
  </section>

  <section class="panel" style="left:336px;top:395px;height:216px">
    <div class="panel-head">Pie 2</div>
    <div style="position:absolute;left:73px;top:56px;width:146px;height:143px;background:#f7f7f7"></div>
    <svg width="134" height="134" viewBox="0 0 42 42" style="position:absolute;left:79px;top:60px">
      <g transform="rotate(-90 21 21)" fill="none" stroke-width="20">
        <circle cx="21" cy="21" r="10" pathLength="100" stroke="#4168e8" stroke-dasharray="3 97"/>
        <circle cx="21" cy="21" r="10" pathLength="100" stroke="#f7cfac" stroke-dasharray="10 90" stroke-dashoffset="-3"/>
        <circle cx="21" cy="21" r="10" pathLength="100" stroke="#48cacb" stroke-dasharray="33 67" stroke-dashoffset="-13"/>
        <circle cx="21" cy="21" r="10" pathLength="100" stroke="#a94cb3" stroke-dasharray="27 73" stroke-dashoffset="-46"/>
        <circle cx="21" cy="21" r="10" pathLength="100" stroke="#93e63c" stroke-dasharray="27 73" stroke-dashoffset="-73"/>
      </g>
    </svg>
    <div class="legend" style="left:230px;top:51px"><i style="background:#4168e8"></i>Series1<br><i style="background:#f7cfac"></i>Series2<br><i style="background:#48cacb"></i>Series3<br><i style="background:#a94cb3"></i>Series4<br><i style="background:#93e63c"></i>Series5<br><i style="background:#2f4cc4"></i>Series6</div>
  </section>

  <section class="panel" style="left:20px;top:629px;height:235px">
    <div class="panel-head">Stat 1</div>
    <div class="search">Search<span></span></div>
    <table>
      <tr><th>Name<span class="sort on">▲</span></th><th>Position<span class="sort">▲▼</span></th><th>Start Date<span class="sort">▲▼</span></th><th>Salary<span class="sort">▲▼</span></th></tr>
      <tr><td>Gerda</td><td>Chefin</td><td>1.11.2013</td><td>Salami</td></tr>
      <tr><td>Gerda</td><td>Chefin</td><td>2.11.2013</td><td>Salami</td></tr>
      <tr><td>Gerda</td><td>Chefin</td><td>3.11.2013</td><td>Salami</td></tr>
      <tr><td>Gerda</td><td>Chefin</td><td>4.11.2013</td><td>Salami</td></tr>
      <tr><td>Gerda</td><td>Chefin</td><td>5.11.2013</td><td>Salami</td></tr>
      <tr><td>Gerda</td><td>Chefin</td><td>6.11.2013</td><td>Salami</td></tr>
    </table>
    <div class="foot">Showing 1 to 6 of 9 entries</div>
    <div class="pager"><span>◂ Previous</span><span class="cur">1</span><span>2</span><span style="border:0">Next ▸</span></div>
  </section>

  <section class="panel" style="left:336px;top:629px;height:235px">
    <div class="panel-head">Stat 2</div>
    <div class="search">Search<span></span></div>
    <table>
      <tr><th>Domain<span class="sort on">▲</span></th><th style="padding-left:4px">Niveau</th><th style="padding-left:4px">Keyw.<span class="sort">▲▼</span></th><th style="padding-left:4px">SE Keyw.<span class="sort">▲▼</span></th></tr>
      <tr><td>domain1.de</td><td style="padding-left:4px"><span class="meter"><b style="width:5px"></b></span></td><td style="padding-left:4px">Gemeinsame Keywords</td><td style="padding-left:4px">SE Keywords</td></tr>
      <tr><td>domain1.de</td><td style="padding-left:4px"><span class="meter"><b style="width:11px"></b></span></td><td style="padding-left:4px">Gemeinsame Keywords</td><td style="padding-left:4px">SE Keywords</td></tr>
      <tr><td>domain1.de</td><td style="padding-left:4px"><span class="meter"><b style="width:18px"></b></span></td><td style="padding-left:4px">Gemeinsame Keywords</td><td style="padding-left:4px">SE Keywords</td></tr>
      <tr><td>domain1.de</td><td style="padding-left:4px"><span class="meter"><b style="width:24px"></b></span></td><td style="padding-left:4px">Gemeinsame Keywords</td><td style="padding-left:4px">SE Keywords</td></tr>
      <tr><td>domain1.de</td><td style="padding-left:4px"><span class="meter"><b style="width:28px"></b></span></td><td style="padding-left:4px">Gemeinsame Keywords</td><td style="padding-left:4px">SE Keywords</td></tr>
      <tr><td>domain1.de</td><td style="padding-left:4px"><span class="meter"><b style="width:31px"></b></span></td><td style="padding-left:4px">Gemeinsame Keywords</td><td style="padding-left:4px">SE Keywords</td></tr>
    </table>
    <div class="foot">Showing 1 to 6 of 9 entries</div>
    <div class="pager"><span>◂ Previous</span><span class="cur">1</span><span>2</span><span style="border:0">Next ▸</span></div>
  </section>

  <section class="panel" style="left:20px;top:883px;height:235px">
    <div class="panel-head">Sternchen</div>
    <div class="search">Search<span></span></div>
    <table>
      <tr><th>Name<span class="sort on">▲</span></th><th>Profilseite<span class="sort">▲▼</span></th><th>Bewertung<span class="sort">▲▼</span></th></tr>
      <tr><td>vimora</td><td>xyz ungelost</td><td></td></tr>
      <tr><td>kelto.de</td><td>xyz ungelost</td><td></td></tr>
      <tr><td>DIE PRAXISWAHL</td><td>xyz ungelost</td><td></td></tr>
      <tr><td>DIE PRAXISWAHL</td><td>xyz ungelost</td><td></td></tr>
      <tr><td>Medsicht</td><td>xyz ungelost</td><td></td></tr>
      <tr><td>reviola</td><td>xyz ungelost</td><td></td></tr>
    </table>
    <div class="foot">Showing 1 to 6 of 10 entries</div>
    <div class="pager"><span>◂ Previous</span><span class="cur">1</span><span>2</span><span style="border:0">Next ▸</span></div>
  </section>
</main>

<footer class="copy">2014 © Medivio</footer>
</body>
</html>
```